Make an Awesome Graphic for a PPT

Attached is the specific content for the project. the X-factor of Adoption. It does not need a title just take the existing graphic an improve it. Attached is our company logo for color palette and the "ugly version". It should look modern and edge in terms of effect and font. Need it by Monday March 7th

```html
<!DOCTYPE html>
<html lang="en">
<head>
<meta charset="UTF-8">
<title>The X-Factor of Adoption</title>
<link href="https://fonts.googleapis.com/css2?family=Montserrat:wght@600;700;800&display=swap" rel="stylesheet">
<style>
  :root {
    --bg: #ffffff;
    --arm-experience: #7d8894;
    --arm-concept-top: #1ba3e1;
    --arm-concept-bottom: #2c3a8e;
    --arm-sentiment: #1565ad;
    --hub-fill: #ffffff;
    --hub-text: #1f4e9f;
    --label: #ffffff;
    --icon-tint: rgba(255, 255, 255, 0.28);
    --hub-icon-tint: rgba(31, 78, 159, 0.16);
  }
  html, body {
    margin: 0;
    padding: 0;
    width: 1200px;
    height: 1200px;
    overflow: hidden;
    background: var(--bg);
  }
  .adoption-graphic {
    display: block;
    width: 1200px;
    height: 1200px;
  }
  .arm-experience { fill: var(--arm-experience); }
  .arm-concept-top { fill: var(--arm-concept-top); }
  .arm-concept-bottom { fill: var(--arm-concept-bottom); }
  .arm-sentiment { fill: var(--arm-sentiment); }
  .arm-label {
    font-family: "Montserrat", sans-serif;
    font-weight: 700;
    font-size: 36px;
    letter-spacing: 0.3px;
    fill: var(--label);
  }
  .arm-icon { fill: var(--icon-tint); }
  .hub-circle { fill: var(--hub-fill); }
  .hub-label {
    font-family: "Montserrat", sans-serif;
    font-weight: 800;
    font-size: 36px;
    letter-spacing: 0.3px;
    fill: var(--hub-text);
  }
  .hub-icon { fill: var(--hub-icon-tint); }
</style>
</head>
<body>
<svg class="adoption-graphic" viewBox="0 0 1200 1200" xmlns="http://www.w3.org/2000/svg" aria-label="The X-factor of adoption diagram">
  <defs>
    <filter id="hub-shadow" x="-30%" y="-30%" width="160%" height="160%">
      <feDropShadow dx="0" dy="4" stdDeviation="10" flood-color="#1b2a4a" flood-opacity="0.25"/>
    </filter>
  </defs>

  <g class="arms">
    <polygon class="arm-experience" points="156,125 569,125 569,557 396,557"/>
    <polygon class="arm-concept-top" points="636,125 1044,125 792,557 636,557"/>
    <polygon class="arm-concept-bottom" points="396,605 569,605 569,1037 156,1037"/>
    <polygon class="arm-sentiment" points="636,605 792,605 1044,1037 636,1037"/>
  </g>

  <g class="arm-labels">
    <text class="arm-label" x="259" y="200">FARMER</text>
    <text class="arm-label" x="259" y="256">EXPERIENCE</text>

    <text class="arm-label" x="730" y="200">INNOVATION</text>
    <text class="arm-label" x="730" y="256">CONCEPT</text>

    <text class="arm-label" x="276" y="897">INNOVATION</text>
    <text class="arm-label" x="276" y="953">CONCEPT</text>

    <text class="arm-label" x="703" y="897">FARMER</text>
    <text class="arm-label" x="703" y="953">SENTIMENT</text>
  </g>

  <g class="arm-icons">
    <circle class="arm-icon" cx="432" cy="350" r="36" role="img" aria-label="Icon: hand holding a star"/>
    <circle class="arm-icon" cx="797" cy="336" r="36" role="img" aria-label="Icon: lightbulb idea"/>
    <circle class="arm-icon" cx="439" cy="768" r="36" role="img" aria-label="Icon: lightbulb idea"/>
    <circle class="arm-icon" cx="792" cy="768" r="36" role="img" aria-label="Icon: happy and unhappy sentiment"/>
  </g>

  <g class="hub">
    <circle class="hub-circle" cx="600" cy="581" r="150" filter="url(#hub-shadow)"/>
    <rect class="hub-icon" x="564" y="466" width="72" height="76" rx="14" role="img" aria-label="Icon: hands reaching together"/>
    <text class="hub-label" x="600" y="612" text-anchor="middle">ADOPTION</text>
    <text class="hub-label" x="600" y="655" text-anchor="middle">ZONE</text>
  </g>
</svg>
</body>
</html>
```